Tazzinetta, the Letter Café is looking for new postcards.

Tazzinetta sells loads of cards and is always looking for new designs. After three years of selling cards produced by others we are now ready to start our own collection.

What is Tazzinetta?
Tazzinetta is a place where you, while drinking coffee or tea, can choose a postcard (we have 300 to 400 different kinds for you to choose from), write it, and have it send on any day you want. We are located in the beautiful city of Leiden, The Netherlands. See enclosed document for more info.

What are we looking for?
Funny, witty, colorful designs that make people smile or think. We are thinking to start out with at least 10 different designs.

The dimensions of the cards are 10 x 14,8 cm, either landscape or portrait. Please enter your design in both pdf and original format (ai. psd. or id. file) where possible in vector.

Designs that are offensive to whatever group of people will be removed immediately.

What's in it for you?
You will become part of the Tazzinetta collection which you can prove because your name will be on the back of the card.
Furthermore we will pay you € 125,- per chosen postcard.

```html
<!DOCTYPE html>
<html lang="en">
<head>
<meta charset="utf-8">
<title>After the Rain, the Sun Will Shine – Postcard</title>
<link rel="stylesheet" href="https://fonts.googleapis.com/css2?family=Federant&family=Nothing+You+Could+Do&display=swap">
<style>
  :root {
    --page-bg: #f4f4f2;
    --sky-top: #7fcdf3;
    --sky-mid: #bfe6f8;
    --sky-low: #e6f5fc;
    --hill-green: #a9d68a;
    --hill-light: #d9efc9;
    --sun-yellow: #fbe98a;
    --title-blue: #24409a;
    --title-orange: #f39a1e;
    --script-ink: #1d1d1d;
    --card-shadow: rgba(0, 0, 0, 0.18);
  }

  * { box-sizing: border-box; margin: 0; padding: 0; }

  html, body {
    width: 1200px;
    height: 900px;
    overflow: hidden;
    background: var(--page-bg);
  }

  .postcard {
    position: absolute;
    left: 330px;
    top: 50px;
    width: 540px;
    height: 800px;
    overflow: hidden;
    box-shadow: 0 2px 10px var(--card-shadow);
  }

  .postcard__sky {
    position: absolute;
    inset: 0;
    background: linear-gradient(180deg, var(--sky-top) 0%, var(--sky-mid) 45%, var(--sky-low) 100%);
  }

  .postcard__scene {
    position: absolute;
    left: 0;
    right: 0;
    bottom: 0;
    height: 455px;
    background:
      radial-gradient(circle at 78% 32%, var(--sun-yellow) 0 22%, transparent 34%),
      linear-gradient(180deg, transparent 0%, transparent 52%, var(--hill-green) 66%, var(--hill-light) 100%);
  }

  .postcard__headline {
    position: absolute;
    top: 52px;
    left: 0;
    right: 0;
    text-align: center;
    font-family: "Federant", serif;
    text-transform: uppercase;
    line-height: 1;
  }

  .headline__rain {
    display: block;
    color: var(--title-blue);
    font-size: 66px;
    letter-spacing: -1px;
  }

  .headline__sun {
    display: block;
    color: var(--title-orange);
    font-size: 64px;
    margin-top: 22px;
    line-height: 0.95;
  }

  .postcard__proverb {
    position: absolute;
    top: 312px;
    left: 0;
    right: 0;
    text-align: center;
    font-family: "Nothing You Could Do", cursive;
    font-size: 18px;
    color: var(--script-ink);
  }
</style>
</head>
<body>
  <main class="postcard">
    <div class="postcard__sky" role="img" aria-label="Blue sky with falling white raindrops"></div>
    <div class="postcard__scene" role="img" aria-label="Illustration of a girl in a purple dress with a purple umbrella walking over green hills beside a smiling rising sun"></div>

    <h1 class="postcard__headline">
      <span class="headline__rain">After the rain,</span>
      <span class="headline__sun">The sun<br>will shine</span>
    </h1>

    <p class="postcard__proverb">(Na regen komt zonneschijn)</p>
  </main>
</body>
</html>
```